KPT Building And Maintenance

Need a very professional looking double sided Buisiness card with all my details phone number, name, email, license number.

Target Market(s)

construction industry

Industry/Entity Type

building

Contact Information for Business Card

Name Dale Whitcombe. Email Address Info@KPTBuilding.example.au mobile number 0452918730 licence number 871406D. web site

```html
<!DOCTYPE html>
<html lang="en">
<head>
<meta charset="utf-8">
<title>KPT Building And Maintenance – Stationery</title>
<link href="https://fonts.googleapis.com/css2?family=Roboto:wght@400;500;700&display=swap" rel="stylesheet">
<style>
  :root {
    --backdrop: #cdcccd;
    --paper: #ffffff;
    --brand-blue: #349cd6;
    --charcoal: #4d5153;
    --ink: #4a4d50;
    --rule: #5a5d60;
  }
  * { margin: 0; padding: 0; box-sizing: border-box; }
  html, body {
    width: 1200px; height: 1022px; overflow: hidden;
    background: var(--backdrop);
    font-family: "Roboto", Arial, sans-serif;
  }
  .canvas { position: relative; width: 1200px; height: 1022px; }

  .sheet, .card {
    position: absolute; background: var(--paper); overflow: hidden;
    box-shadow: 0 8px 18px rgba(0,0,0,0.22);
  }
  .bands { position: absolute; inset: 0; width: 100%; height: 100%; }
  .band-blue { fill: var(--brand-blue); }
  .band-dark { fill: var(--charcoal); }

  .wordmark {
    position: absolute; font-weight: 700; color: var(--charcoal);
    text-transform: uppercase; line-height: 1.05; letter-spacing: 0.06em;
    display: flex; align-items: center; gap: 7px; white-space: nowrap;
  }
  .wordmark-mark { display: inline-block; background: var(--brand-blue); border-radius: 50%; flex: none; }
  .wordmark.on-blue { color: #fff; }
  .wordmark.on-blue .wordmark-mark { background: #fff; }

  .icon { width: 8px; height: 8px; flex: none; fill: currentColor; }
  .icon.outline { fill: none; stroke: currentColor; stroke-width: 1.5; }

  /* Letterhead */
  .letterhead { left: 90px; top: 91px; width: 568px; height: 804px; }
  .letterhead .wordmark { left: 32px; top: 52px; font-size: 15px; }
  .letterhead .wordmark-mark { width: 18px; height: 18px; }
  .header-rule {
    position: absolute; left: 267px; right: 0; top: 80px; height: 4px;
    border-top: 1.5px solid var(--rule); border-bottom: 1.5px solid var(--rule);
  }
  .letterhead-contacts {
    position: absolute; left: 33px; top: 747px; display: flex;
    color: #fff; font-size: 9px;
  }
  .contact-col { display: flex; flex-direction: column; gap: 7px; }
  .contact-col + .contact-col {
    margin-left: 14px; padding-left: 14px; border-left: 1px solid rgba(255,255,255,0.85);
  }
  .contact { display: flex; align-items: center; gap: 5px; height: 9px; }

  /* Cards */
  .card { width: 303px; height: 173px; left: 781px; }
  .card-front { top: 259px; }
  .card-front .wordmark { left: 48px; top: 66px; font-size: 13px; }
  .card-front .wordmark-mark { width: 16px; height: 16px; }
  .card-front .card-web {
    position: absolute; left: 21px; top: 141px; color: #fff; font-size: 11px;
    display: flex; align-items: center; gap: 6px;
  }
  .card-front .card-web .icon { width: 9px; height: 9px; }

  .card-back { top: 512px; }
  .holder-name {
    position: absolute; left: 20px; top: 19px; color: var(--brand-blue);
    font-weight: 500; font-size: 14px; letter-spacing: 0.01em; text-transform: uppercase;
  }
  .holder-role { position: absolute; left: 21px; top: 38px; color: var(--ink); font-size: 11px; }
  .card-details {
    position: absolute; left: 122px; top: 41px; list-style: none;
    color: var(--ink); font-size: 10.5px; white-space: nowrap;
  }
  .card-details li { display: flex; align-items: center; gap: 7px; height: 20.5px; }
  .card-details .icon { width: 9px; height: 9px; color: var(--brand-blue); }
  .card-back .wordmark { left: 20px; top: 134px; font-size: 8.5px; gap: 5px; }
  .card-back .wordmark-mark { width: 11px; height: 11px; }
</style>
</head>
<body>
<div class="canvas">

  <!-- Letterhead -->
  <section class="sheet letterhead" aria-label="Letterhead">
    <svg class="bands" viewBox="0 0 568 804" preserveAspectRatio="none" aria-hidden="true">
      <polygon class="band-blue" points="0,698 568,778 568,804 0,804"/>
      <polygon class="band-dark" points="405,755 568,715 568,778"/>
    </svg>
    <div class="wordmark"><span class="wordmark-mark"></span><span>KPT Building and<br>Maintenance</span></div>
    <div class="header-rule"></div>
    <div class="letterhead-contacts">
      <div class="contact-col">
        <span class="contact"><svg class="icon" viewBox="0 0 16 16"><path d="M3 1l3 3-2 2c1 2 3 4 5 5l2-2 3 3-2 3C7 15 1 9 1 3z"/></svg>045 291 8730</span>
        <span class="contact"><svg class="icon" viewBox="0 0 16 16"><path d="M15 1L1 7l5 2 2 6z"/></svg>Info@KPTBuilding.example.au</span>
      </div>
      <div class="contact-col">
        <span class="contact"><svg class="icon outline" viewBox="0 0 16 16"><circle cx="8" cy="8" r="6.5"/><ellipse cx="8" cy="8" rx="3" ry="6.5"/><path d="M1.5 8h13"/></svg>KPTBuilding.example.au</span>
        <span class="contact"><svg class="icon outline" viewBox="0 0 16 16"><rect x="1" y="3" width="14" height="10"/><path d="M9 6h4M9 9h4M3 10h4"/><circle cx="5" cy="6.5" r="1.3"/></svg>871406D</span>
      </div>
    </div>
  </section>

  <!-- Business card front -->
  <section class="card card-front" aria-label="Business card front">
    <svg class="bands" viewBox="0 0 303 173" preserveAspectRatio="none" aria-hidden="true">
      <polygon class="band-blue" points="0,112 303,160 303,173 0,173"/>
      <polygon class="band-dark" points="224,147.5 303,129 303,160"/>
    </svg>
    <div class="wordmark"><span class="wordmark-mark"></span><span>KPT Building and<br>Maintenance</span></div>
    <div class="card-web"><svg class="icon outline" viewBox="0 0 16 16"><circle cx="8" cy="8" r="6.5"/><ellipse cx="8" cy="8" rx="3" ry="6.5"/><path d="M1.5 8h13"/></svg>KPTBuilding.example.au</div>
  </section>

  <!-- Business card back -->
  <section class="card card-back" aria-label="Business card back">
    <svg class="bands" viewBox="0 0 303 173" preserveAspectRatio="none" aria-hidden="true">
      <polygon class="band-blue" points="0,97 303,166 303,173 0,173"/>
      <polygon class="band-dark" points="212,145.3 303,124 303,166"/>
    </svg>
    <div class="holder-name">Dale Whitcombe</div>
    <div class="holder-role">CEO</div>
    <ul class="card-details">
      <li><svg class="icon" viewBox="0 0 16 16"><path d="M3 1l3 3-2 2c1 2 3 4 5 5l2-2 3 3-2 3C7 15 1 9 1 3z"/></svg>045 291 8730</li>
      <li><svg class="icon" viewBox="0 0 16 16"><path d="M15 1L1 7l5 2 2 6z"/></svg>Info@KPTBuilding.example.au</li>
      <li><svg class="icon outline" viewBox="0 0 16 16"><circle cx="8" cy="8" r="6.5"/><ellipse cx="8" cy="8" rx="3" ry="6.5"/><path d="M1.5 8h13"/></svg>KPTBuilding.example.au</li>
      <li><svg class="icon outline" viewBox="0 0 16 16"><rect x="1" y="3" width="14" height="10"/><path d="M9 6h4M9 9h4M3 10h4"/><circle cx="5" cy="6.5" r="1.3"/></svg>871406D</li>
    </ul>
    <div class="wordmark on-blue"><span class="wordmark-mark"></span><span>KPT Building and<br>Maintenance</span></div>
  </section>

</div>
</body>
</html>
```